Plastic Aesthetic and Reconstructive Surgery

I need a double sided luxurius Business Card, with a minimal, modern design focused on my job.
Besides my Name, Surname and contact information, the use of my initials (M and T) in free style combination as a logo will help.
In the one side all data written in English.
In the other side written in Greek if possible.
Please feel free to use the letter type and size you prefer.
Please use icons type and size and orientation you like.
The Name, Surname, occupation and the initials can be UV spotted.
You can use also in the background a texture or something that will make the card luxurious.
I would prefer pal colors.
Each side can have different colors or even better they can be reversed or inverted
As I have said you can use the wet sand color, light brown, dark brown, gold, light gold, white
Updates

Need extra days to review

i am waiting for some new ideas and some modifications from the designers. I need a couple of days extention of the period for the designers to post their modifications.

Target Market(s)

Patients who need a reconstructive intervention or surgery. Also people, mainly women, that they need aesthetic or cosmetic interventions to face or body

Contact Information for Business Card

Name and surname, occupation, member of an organization , mobile telephone number, Mail, Tessera and Lumora accounts

Font styles to use
Script
Other font styles liked:
• Gabriola

Colors
FFC000
F8CF3A
FAE287
FDF2CF
FEFAEE

Requirements
Must have
• A free combination of my initials (M and T) as a logo
Nice to have
• Fade out with the background colors, UV spotted of the name, initials logo
Should not have
• Address

```html
<!DOCTYPE html>
<html lang="en">
<head>
<meta charset="utf-8">
<title>Markos Theodorou — Business Card</title>
<link href="https://fonts.googleapis.com/css2?family=Raleway:wght@500;800&family=Commissioner:wght@400;600;800&display=swap" rel="stylesheet">
<style>
  :root {
    --page: #ffffff;
    --sand: #c3976f;
    --sand-deep: #a67b5e;
    --sand-light: #d8b894;
    --white: #ffffff;
    --icon-tone: #e3b372;
  }
  * { box-sizing: border-box; margin: 0; padding: 0; }
  html, body {
    width: 1200px; height: 1200px; overflow: hidden;
    background: var(--page);
  }
  .canvas { position: relative; width: 1200px; height: 1200px; }

  .card {
    position: absolute; left: 186px; width: 835px; height: 477px;
    border-radius: 31px; background: var(--sand); overflow: hidden;
    color: var(--white);
    font-variant-numeric: lining-nums;
  }
  .card--front { top: 87px; }
  .card--back { top: 643px; }

  /* shared monogram */
  .monogram {
    position: absolute; border-radius: 50%;
    background: var(--sand-deep);
    display: flex; align-items: center; justify-content: center;
    color: var(--sand-light);
    font-family: "Raleway", sans-serif; font-weight: 500;
    letter-spacing: 0.02em;
  }

  /* front */
  .front-texture {
    position: absolute; inset: 0;
    background: linear-gradient(160deg, rgba(226,196,176,0.18), rgba(226,196,176,0.04) 60%, rgba(226,196,176,0.14));
  }
  .card--front .monogram {
    left: 334px; top: 92px; width: 166px; height: 166px; font-size: 96px;
  }
  .front-name {
    position: absolute; left: 0; right: 0; top: 290px; text-align: center;
    font-family: "Raleway", sans-serif; font-weight: 800;
    font-size: 35px; line-height: 42px; letter-spacing: 0.18em;
    white-space: nowrap;
  }
  .front-specialty {
    position: absolute; left: 0; right: 0; top: 340px; text-align: center;
    font-family: "Raleway", sans-serif; font-weight: 500;
    font-size: 22px; letter-spacing: 0.13em;
    white-space: nowrap;
  }
  .front-phone-rule {
    position: absolute; top: 440px; height: 3px; background: var(--white);
  }
  .front-phone-rule--left { left: 0; width: 296px; }
  .front-phone-rule--right { left: 539px; right: 0; }
  .front-phone {
    position: absolute; left: 296px; width: 243px; top: 426px; text-align: center;
    font-family: "Raleway", sans-serif; font-weight: 800;
    font-size: 21px; line-height: 26px; letter-spacing: 0.1em;
  }

  /* back */
  .back-texture {
    position: absolute; left: 0; top: 0; width: 400px; height: 100%;
    background: linear-gradient(90deg, rgba(226,196,176,0.22), rgba(226,196,176,0.08) 55%, rgba(226,196,176,0) 100%);
  }
  .back-identity {
    position: absolute; left: 189px; top: 118px;
    font-family: "Commissioner", sans-serif;
  }
  .back-name {
    font-weight: 400; font-size: 28px; letter-spacing: 0.1em; line-height: 1.2;
    white-space: nowrap;
  }
  .back-name strong { font-weight: 800; }
  .back-role {
    font-weight: 400; font-size: 18.5px; letter-spacing: 0.12em; line-height: 32px;
    margin-top: 4px; white-space: nowrap;
  }
  .contact {
    position: absolute; display: flex; align-items: center; gap: 8px;
    font-family: "Commissioner", sans-serif;
  }
  .contact__badge {
    width: 38px; height: 38px; border-radius: 50%; background: var(--white);
    flex: none; display: flex; align-items: center; justify-content: center;
  }
  .contact__badge svg { width: 22px; height: 22px; }
  .contact__label { font-weight: 600; font-size: 14px; line-height: 17px; }
  .contact__value { font-weight: 400; font-size: 14px; letter-spacing: 0.14em; line-height: 17px; white-space: nowrap; }
  .contact--social { left: 189px; top: 256px; }
  .contact--email { left: 455px; top: 256px; align-items: flex-start; }
  .contact--gallery { left: 189px; top: 344px; }
  .contact--phone { left: 455px; top: 344px; }
  .card--back .monogram {
    left: 695px; top: 336px; width: 106px; height: 106px; font-size: 56px;
  }
</style>
</head>
<body>
<div class="canvas">

  <section class="card card--front" aria-label="Business card, English side">
    <div class="front-texture" role="img" aria-label="Fine geometric cube line pattern over the card"></div>
    <div class="monogram">MT</div>
    <h1 class="front-name">Markos Theodorou, MD, MSc</h1>
    <p class="front-specialty">Plastic Reconstructive and Aesthetic Surgery</p>
    <span class="front-phone-rule front-phone-rule--left"></span>
    <p class="front-phone">+30 690 218 4407</p>
    <span class="front-phone-rule front-phone-rule--right"></span>
  </section>

  <section class="card card--back" aria-label="Business card, Greek side" lang="el">
    <div class="back-texture" role="img" aria-label="Faint low-poly line network along the left edge"></div>

    <div class="back-identity">
      <h2 class="back-name">Μάρκος Θεοδώρου<strong>, MD, MSc</strong></h2>
      <p class="back-role">Αισθητική και Επανορθωτική Πλαστική Χειρουργική<br>Χειρουργική Μέλος Ε.Σ.Κ.Α.Χ</p>
    </div>

    <div class="contact contact--social" lang="en">
      <span class="contact__badge"></span>
      <div>
        <p class="contact__label">Tessera ID</p>
        <p class="contact__value">Your address Here</p>
      </div>
    </div>

    <div class="contact contact--email" lang="en">
      <span class="contact__badge">
        <svg viewBox="0 0 24 24" fill="none" stroke="var(--icon-tone)" stroke-width="1.4">
          <rect x="3" y="6" width="18" height="12" rx="2"/>
          <path d="M3.5 7l8.5 6 8.5-6"/>
        </svg>
      </span>
      <div>
        <p class="contact__label">Email Address</p>
        <p class="contact__value">m.theodorou.clinic<br>@mailbox.gr</p>
      </div>
    </div>

    <div class="contact contact--gallery" lang="en">
      <span class="contact__badge"></span>
      <div>
        <p class="contact__label">Visit Lumora</p>
        <p class="contact__value">www.theodorou-clinic.gr</p>
      </div>
    </div>

    <div class="contact contact--phone" lang="en">
      <span class="contact__badge">
        <svg viewBox="0 0 24 24" fill="var(--icon-tone)">
          <path d="M6.6 3.5c.6-.4 1.4-.3 1.8.3l1.7 2.6c.4.6.3 1.3-.2 1.8l-1.2 1.1c.9 2 2.4 3.6 4.4 4.6l1.1-1.2c.5-.5 1.2-.6 1.8-.2l2.6 1.6c.6.4.8 1.2.4 1.8l-.9 1.5c-.6 1-1.8 1.5-2.9 1.2C9.7 17.5 6.2 14 4.6 8.5c-.3-1.1.2-2.3 1.2-2.9z"/>
        </svg>
      </span>
      <div>
        <p class="contact__label">Office Number</p>
        <p class="contact__value">+30 690 218 4407</p>
      </div>
    </div>

    <div class="monogram">MT</div>
  </section>

</div>
</body>
</html>
```